Hot young IT advisor needs business cards as upscale and innovative as they are

We need business cards that make a statement about who we are, as a young and upscale IT advisor. Our whole angle is innovation and tenacity in our personal relationships with our clients. We've just done a brand overhaul and need cards that have the new logos, but we're also looking for someone with a sixth sense who can capture what sets us apart and communicate that with a business card. Clean, minimalist, upscale, innovative, personal. Our budget only allows room for them to be soft-touch, no spot gloss or foil designs please.

Target Market(s)

High-level decision makers at middle-market and large organizations in the healthcare, financial services, sports and entertainment, K-12 education, college and university, state and local government, and federal government sectors.

Industry/Entity Type

Information Technology

Font styles to use
Sans Serif

Colors
ec1f27
606060
ffffff

Requirements
Should not have
• Designs with low contrast which would require spot-gloss or embossing.

```html
<!DOCTYPE html>
<html lang="en">
<head>
<meta charset="utf-8">
<title>Northvale Business Cards</title>
<link rel="stylesheet" href="https://fonts.googleapis.com/css2?family=Open+Sans:wght@400;600;700&family=Montserrat:wght@500&display=swap">
<style>
  :root {
    --brand-red: #ec1f27;
    --ink-grey: #606060;
    --ink-dark: #2b2b2b;
    --paper: #ffffff;
    --backdrop: #2a2a2c;
  }
  * { box-sizing: border-box; margin: 0; padding: 0; }
  html, body { width: 1200px; height: 960px; overflow: hidden; }
  body {
    background: var(--backdrop);
    font-family: "Open Sans", Arial, sans-serif;
    position: relative;
  }
  .card {
    position: absolute;
    left: 240px;
    width: 720px;
    height: 411px;
    background: var(--paper);
    box-shadow: 0 10px 30px rgba(0,0,0,0.45);
  }
  .card--front { top: 46px; }
  .card--back { top: 503px; }

  /* Front */
  .front-brand {
    position: absolute;
    left: 0; right: 0; top: 150px;
    display: flex; justify-content: center; align-items: center; gap: 16px;
  }
  .brand-square {
    width: 30px; height: 30px; background: var(--brand-red);
  }
  .brand-name {
    font-family: "Montserrat", Arial, sans-serif;
    font-weight: 500;
    font-size: 46px;
    letter-spacing: 6px;
    color: var(--ink-grey);
    text-transform: uppercase;
  }
  .front-url {
    position: absolute;
    left: 0; right: 0; top: 250px;
    text-align: center;
    font-size: 15px;
    letter-spacing: 5px;
    color: var(--ink-grey);
  }

  /* Back */
  .back-brand {
    position: absolute;
    left: 40px; top: 175px;
    display: flex; align-items: center; gap: 12px;
  }
  .back-brand .brand-square { width: 22px; height: 22px; }
  .back-brand .brand-name { font-size: 30px; letter-spacing: 3px; }
  .divider {
    position: absolute;
    left: 340px; top: 70px;
    width: 1px; height: 270px;
    background: linear-gradient(to bottom, rgba(96,96,96,0), var(--ink-grey) 30%, var(--ink-grey) 70%, rgba(96,96,96,0));
  }
  .contact {
    position: absolute;
    left: 375px; top: 72px;
    color: var(--ink-dark);
  }
  .contact__name { font-size: 26px; font-weight: 700; line-height: 1.1; }
  .contact__title { font-size: 19px; color: var(--brand-red); margin-bottom: 10px; }
  .contact__address { font-size: 17px; line-height: 1.35; margin-bottom: 8px; }
  .contact__list { list-style: none; font-size: 17px; line-height: 1.5; }
  .contact__list li { display: flex; align-items: center; gap: 10px; }
  .contact__list svg { width: 16px; height: 16px; fill: var(--ink-dark); flex: none; }
</style>
</head>
<body>
  <section class="card card--front">
    <div class="front-brand">
      <span class="brand-square"></span>
      <span class="brand-name">Northvale</span>
    </div>
    <p class="front-url">www.northvale.example</p>
  </section>

  <section class="card card--back">
    <div class="back-brand">
      <span class="brand-square"></span>
      <span class="brand-name">Northvale</span>
    </div>
    <div class="divider"></div>
    <div class="contact">
      <p class="contact__name">Evan Carter</p>
      <p class="contact__title">President</p>
      <p class="contact__address">1420 Linden Court<br>Maple Heights, NY 10990</p>
      <ul class="contact__list">
        <li><svg viewBox="0 0 16 16"><path d="M2 5c0-2 2-3 6-3s6 1 6 3v1h-3V5H5v1H2zM4 7h8l2 7H2z"/></svg>(555) 0142-7781</li>
        <li><svg viewBox="0 0 16 16"><path d="M4 1h8v14H4zM5.5 2.5v9h5v-9z"/></svg>(555) 0187-3306</li>
        <li><svg viewBox="0 0 16 16"><path d="M4 1h8v4H4zM1 6h14v7h-3v2H4v-2H1zM5 10v4h6v-4z"/></svg>(555) 0119-4452</li>
        <li><svg viewBox="0 0 16 16"><path d="M1 3h14v10H1zM2.5 4.5 8 9l5.5-4.5z"/></svg>hello@northvale.example</li>
        <li><svg viewBox="0 0 16 16"><circle cx="8" cy="8" r="7"/></svg>www.northvale.example</li>
      </ul>
    </div>
  </section>
</body>
</html>
```